Signage Design Project

we embroider logos on to own garments and our garments

we aim to turn around items in about 1 hour

morning we are quicker about 1 hour

afternoons work build s up take a longer 2- 3 hours

i want to tell people they can pick up bargain clothing
in our local super market
bring it to our drive thu window pay £2.99 per item
and have their logo embroidered and collect them in hours !!

we have spent a lot of money building machine
capacity to offer this service

the big buyers of clothing are the
main major super markets
there power to get the prices down is huge

i have been offered a sign position in hallidays super market

i need to make it clear to any nationality
especially non english speakers or readers

the new small business start ups in my area is huge

they have little money to get started
so a very cheap way logo embroidered on to bargain clothes
will entice a lot of start ups to us

our logo we use it horizontal and vertical depending on the sign shape

we have a u tube video

prime kettle

explains a little what we do

Target Market(s)

start up businesses

Industry/Entity Type

Small Business

Requirements
Must have
• must be easy to understand
by any nationality
in my area
we have thousands of hard working people from all over the world

sign
size is
6 feet high
4 feet wide

we advertise our logo
prime kettle
with 30 road side bill boards and 10 round abouts with signs

so it is quiet strong in my catchment area

```html
<!DOCTYPE html>
<html lang="en">
<head>
<meta charset="utf-8">
<title>Prime Kettle – Embroidery Sign</title>
<link rel="stylesheet" href="https://fonts.googleapis.com/css2?family=Arimo:wght@400&display=swap">
<style>
  :root {
    --page: #ffffff;
    --ink: #000000;
    --frame: #000000;
    --brand-blue: #2c3590;
  }
  * { margin: 0; padding: 0; box-sizing: border-box; }
  html, body {
    width: 1200px;
    height: 1000px;
    overflow: hidden;
    background: var(--page);
  }
  .canvas {
    position: relative;
    width: 1200px;
    height: 1000px;
    background: var(--page);
    font-family: "Arimo", Arial, sans-serif;
    color: var(--ink);
  }
  .sign {
    position: absolute;
    left: 238px;
    top: 0;
    width: 681px;
    height: 1000px;
    border: 2px solid var(--frame);
    border-bottom: none;
  }
  .brand {
    position: absolute;
    left: 62px;
    top: 24px;
    width: 556px;
    height: 248px;
    display: flex;
    align-items: center;
    justify-content: center;
    gap: 18px;
  }
  .brand-mark {
    width: 40px;
    height: 40px;
    background: var(--brand-blue);
    flex: none;
  }
  .brand-name {
    font-size: 48px;
    font-weight: 400;
    line-height: 1;
    color: var(--ink);
    white-space: nowrap;
  }
  .intro {
    position: absolute;
    left: 54px;
    font-size: 20px;
    line-height: 29px;
  }
  .intro--love { top: 322px; }
  .intro--offer { top: 418px; }
  .service {
    position: absolute;
    left: 54px;
    font-size: 27px;
    line-height: 35px;
  }
  .service--early { top: 519px; }
  .service--afternoon { top: 590px; }
  .service--designs { top: 662px; }
  .service--text { top: 734px; }
  .contact {
    position: absolute;
    left: 0;
    width: 592px;
    top: 842px;
    text-align: center;
    font-size: 27px;
    line-height: 36px;
    font-style: normal;
  }
</style>
</head>
<body>
<main class="canvas">
  <section class="sign">
    <header class="brand">
      <span class="brand-mark"></span>
      <h1 class="brand-name">Prime Kettle</h1>
    </header>

    <p class="intro intro--love">We at PRIME KETTLE love Hallidays’ bargains!<br>Their garments are easy to embroider.</p>
    <p class="intro intro--offer">We will emborider your logo for £2.99 per item<br>if you quote “I love Hallidays!” at the drive through.</p>

    <p class="service service--early">Early Birds [before noon]: 1 Hour</p>
    <p class="service service--afternoon">Afternoon: 2 Hours</p>
    <p class="service service--designs">New Designs @ £10.99 / 4 hours</p>
    <p class="service service--text">Text only logos are free, done instore<br>with no wait!</p>

    <address class="contact">
      412-414 Marlow Road<br>
      Enfield&nbsp; EN3 9QX<br>
      01632 960418<br>
      sales@primekettle.co.uk
    </address>
  </section>
</main>
</body>
</html>
```